Коробки для строительного крепежа LUM-ARK
Задание на дизайн
Приоритеты объектов в упаковке
Знак производителя, Марка продукта, Вид продукта, Название продукта, Иллюстрация
Опишите свою организацию или продукт и целевую аудиторию
Люмарк - крупнейший в РФ производитель крепежа для стройки, производства мебели и деревянной тары различного назначения. Крепеж позиционируется под маркой LUM-ARK. Также компания продает и предоставляет в аренду инструмент (пневмо, электро, газовый) и компрессоры под собственной маркой Kaito. Этот инструмент специально разработан для забивания крепежа марки LUM-ARK.
Сайт компании: lum-ark.ru
фото инструмента для забивания основного продукта - гвоздь D34 - который фасуется в коробки
основной продукт - гвоздь D34 - который фасуется в коробки
Такой стиль оформления коробок нравится
Такой стиль оформления коробок НЕ нравится (ранее были наши коробки)
Такой стиль оформления коробок НЕ нравится (сейчас у нас такие коробки)
Такой стиль оформления боксов НЕ нравится (сейчас у нас такие боксы)
Примерно так нужно показать развернутую коробку и подписать длину всех сторон в мм
Так можно отобразить подпись Professional к базовому логотипу LUM-ARK
Стикер - наклейка на коробку с указанием количества и типоразмера гвоздя. Используется при фасовке. Наклеивается на коробки, так как в одну и ту же коробку может фасоваться гвоздь разной длины и толщины (соотв количество тоже помещается разное). Желательно сразу выделить в дизайне коробки место, куда размещать стикер. Можно его сразу вставить в макет. Размер 58х60мм
Комментарии и пожелания для дизайнеров
брендбук Люмарк - https://files.example-store.ru/i/QwErTy8K452pLm
(можно предложить в оформлении другие цвета для заливки фона, не только указанные в брендбуке)
ТЗ на разработку упаковки - https://files.example-store.ru/i/bnMxLp3Rt7wsza

```html
<!DOCTYPE html>
<html lang="ru">
<head>
<meta charset="utf-8">
<title>LUM-ARK — коробка, развёртка</title>
<link rel="stylesheet" href="https://fonts.googleapis.com/css2?family=Montserrat:wght@600;700;800&display=swap">
<style>
  :root {
    --brand-green: #a0bf2c;
    --brand-green-light: #c3d86e;
    --ink: #231f20;
    --paper: #ffffff;
  }
  html, body {
    margin: 0;
    padding: 0;
    width: 1200px;
    height: 944px;
    overflow: hidden;
    background: var(--paper);
    font-family: "Montserrat", Arial, sans-serif;
  }
  .dieline {
    position: relative;
    width: 1200px;
    height: 944px;
  }
  .panel { position: absolute; }
  .flap-top   { left: 330px; top: 83px;  width: 532px; height: 179px; background: var(--brand-green); }
  .side-left  { left: 116px; top: 262px; width: 214px; height: 418px; background: var(--brand-green); }
  .face-front { left: 330px; top: 262px; width: 243px; height: 418px; background: var(--paper); }
  .pattern-field {
    background: linear-gradient(135deg, var(--brand-green) 0%, var(--brand-green-light) 50%, var(--brand-green) 100%);
  }
  .face-pattern { left: 573px; top: 262px; width: 503px; height: 418px; }
  .flap-bottom  { left: 330px; top: 686px; width: 532px; height: 167px; }

  .brand {
    position: absolute;
    display: flex;
    flex-direction: column;
    align-items: flex-start;
  }
  .brand-row { display: flex; align-items: center; gap: 7px; }
  .brand-square { width: 14px; height: 14px; background: var(--brand-green); }
  .brand-name {
    font-weight: 800;
    font-size: 34px;
    line-height: 1;
    color: var(--ink);
    letter-spacing: 0.5px;
  }
  .brand-tagline {
    margin-top: 6px;
    font-weight: 800;
    font-size: 9.5px;
    color: var(--ink);
    letter-spacing: 0.2px;
  }
  .brand-front  { left: 386px; top: 308px; }
  .brand-bottom { left: 386px; top: 748px; }
  .brand-bottom .brand-square { background: var(--ink); }

  .product-category {
    position: absolute;
    left: 372px;
    top: 451px;
    margin: 0;
    font-weight: 700;
    font-size: 30px;
    line-height: 34px;
    color: var(--ink);
    white-space: nowrap;
  }
  .product-name {
    position: absolute;
    left: 373px;
    top: 533px;
    margin: 0;
    font-weight: 700;
    font-size: 20px;
    color: var(--brand-green);
  }
</style>
</head>
<body>
  <main class="dieline">
    <div class="panel flap-top"></div>
    <div class="panel side-left"></div>
    <section class="panel face-front"></section>
    <div class="panel face-pattern pattern-field" role="img" aria-label="Повторяющийся фирменный узор из букв на зелёном фоне"></div>
    <div class="panel flap-bottom pattern-field" role="img" aria-label="Повторяющийся фирменный узор из букв на зелёном фоне"></div>

    <div class="brand brand-front">
      <div class="brand-row"><span class="brand-name">LUM-ARK</span><span class="brand-square"></span></div>
      <span class="brand-tagline">ТЕХНОЛОГИЯ КРЕПЕЖА</span>
    </div>

    <h1 class="product-category">Строительный<br>Крепеж</h1>
    <p class="product-name">Гвоздь D34</p>

    <div class="brand brand-bottom">
      <div class="brand-row"><span class="brand-name">LUM-ARK</span><span class="brand-square"></span></div>
      <span class="brand-tagline">ТЕХНОЛОГИЯ КРЕПЕЖА</span>
    </div>
  </main>
</body>
</html>
```